Sneaker Company looking for a partner on multiple packaging designs!

We are a company who is passionate about Sneakers and quality products! This project is the first of many packaging designs we will need. We have our logo (see attached) and we would like the background to be all black for this package. I'm working on the UPC number right now so please leave a space for the UPC. Where we need some help is the overall design and some "marketing" word smithing. We are hoping to find a partner that we can work with on future products as well who really understands us and our products! Our company name is Kolvu and this first product will be for crease protection. They are known at Crease Guards, Crease Protection, Anti-Crease Inserts, etc...Not sure the right name to go with but would love some feedback! The package will have 2 Pairs inside. (One Black and One white). This product is something you slide into the shoe while you are wearing it. This product helps prevent the creasing of the toe box. Basically to help keep the sneaker clean and crisp! They are labeled L and R for Left and Right. They are also thin enough that you can trim them with scissors to fit! I have much more to share but before adding all the marketing words, if this is a project you would like to take on please message me and let’s chat! I want to make sure this is a good fit for both of us. Please do not submit projects without speaking to me first. If doing so that means you didn’t read this and you will immediately be removed from contention.

Thank you and look forward to working with you!
Marcus

Target Market(s)

Customers who love Sneakers

Industry/Entity Type

Retail

Font styles to use
Sans Serif

Requirements
Must have
• Clean, Original and Simple
Nice to have
• Pretty open!
Should not have
• Anything copied from another product. No more than 4 colors total on the box.

```html
<!DOCTYPE html>
<html lang="en">
<head>
<meta charset="utf-8">
<title>Kolvu Crease Guards – Box Dieline</title>
<link rel="stylesheet" href="https://fonts.googleapis.com/css2?family=Orbitron:wght@500;700&display=swap">
<style>
  :root {
    --paper: #ffffff;
    --box: #000000;
    --panel-shade: #1b1b1c;
    --mint: #3ec395;
    --steel: #6d6d70;
    --fold: #ffffff;
    --sketch: #2a2a2c;
  }
  html, body {
    margin: 0;
    padding: 0;
    width: 900px;
    height: 1200px;
    overflow: hidden;
    background: var(--paper);
  }
  .dieline {
    position: relative;
    width: 900px;
    height: 1200px;
    font-family: "Orbitron", sans-serif;
  }
  .dieline-art {
    position: absolute;
    inset: 0;
  }
  .brand-name {
    position: absolute;
    margin: 0;
    color: var(--mint);
    font-weight: 500;
    letter-spacing: 2px;
    line-height: 1;
    white-space: nowrap;
  }
  .brand-name--lid { left: 240px; top: 207px; font-size: 28px; }
  .brand-name--flap { left: 161px; top: 310px; font-size: 24px; transform: translate(-50%, -50%) rotate(90deg); }
  .brand-name--front { left: 558px; top: 515px; font-size: 22px; }
  .brand-name--end { left: 738px; top: 735px; font-size: 26px; transform: translate(-50%, -50%) rotate(-90deg); }
  .brand-name--back { left: 280px; top: 939px; font-size: 22px; transform: translate(-50%, -50%) rotate(180deg); }

  .tagline {
    position: absolute;
    right: 237px;
    top: 186px;
    margin: 0;
    color: var(--mint);
    font-size: 12.5px;
    font-weight: 500;
    line-height: 18px;
    text-align: right;
    letter-spacing: 0.6px;
  }
  .product-title {
    position: absolute;
    margin: 0;
    line-height: 1;
    letter-spacing: 3px;
    white-space: nowrap;
  }
  .product-title span { display: block; }
  .product-title .solid { color: var(--mint); font-weight: 700; }
  .product-title .outline {
    color: transparent;
    -webkit-text-stroke: 1.3px var(--mint);
    font-weight: 500;
  }
  .product-title--lid { left: 240px; top: 358px; font-size: 40px; }
  .product-title--lid .outline { margin-top: 8px; font-size: 40px; }
  .product-title--back {
    left: 340px; top: 904px; font-size: 37px; text-align: right;
    transform: rotate(180deg);
    transform-origin: 110px 40px;
  }
  .product-title--back .outline { margin-top: 8px; }

  .size-mark {
    position: absolute;
    left: 640px;
    top: 406px;
    margin: 0;
    color: var(--fold);
    font-size: 28px;
    font-weight: 500;
    line-height: 1;
  }
  .shoe-art {
    position: absolute;
    background: linear-gradient(135deg, var(--sketch), #141415);
    border-radius: 6px;
  }
  .shoe-art--lid { left: 515px; top: 266px; width: 118px; height: 190px; }
  .shoe-art--front { left: 226px; top: 494px; width: 74px; height: 90px; }
  .shoe-art--back { left: 600px; top: 886px; width: 76px; height: 90px; }

  .upc-space {
    position: absolute;
    left: 395px;
    top: 494px;
    width: 112px;
    height: 58px;
    background: var(--paper);
  }
</style>
</head>
<body>
<main class="dieline">
  <svg class="dieline-art" width="900" height="1200" viewBox="0 0 900 1200" aria-hidden="true">
    <polygon class="box-body" fill="var(--box)" points="52.8,145.8 692.4,145.8 692.4,444 805.2,444 805.2,571.2 847.2,571.2 847.2,898.2 805.2,898.2 805.2,1026 691.8,1026 691.8,1054.2 208.8,1054.2 208.8,1026 95.4,1026 95.4,868.2 208.8,868.2 208.8,600.6 95.4,600.6 95.4,473.4 52.8,473.4"/>
    <g class="panel-shade" fill="var(--panel-shade)">
      <rect x="300" y="612" width="300" height="246"/>
    </g>
    <g class="fold-lines" fill="none" stroke="var(--fold)" stroke-width="0.8">
      <rect x="67.8" y="160.8" width="609.6" height="297.6"/>
      <line x1="96" y1="160.8" x2="96" y2="458.4"/>
      <line x1="223.8" y1="160.8" x2="223.8" y2="458.4"/>
      <rect x="110.4" y="458.4" width="679.8" height="127.8"/>
      <line x1="223.8" y1="458.4" x2="223.8" y2="586.2"/>
      <line x1="677.4" y1="458.4" x2="677.4" y2="586.2"/>
      <rect x="223.8" y="586.2" width="453.6" height="297.6"/>
      <rect x="677.4" y="586.2" width="155.4" height="297.6"/>
      <line x1="804" y1="586.2" x2="804" y2="883.8"/>
      <rect x="110.4" y="883.8" width="679.8" height="127.2"/>
      <line x1="223.8" y1="883.8" x2="223.8" y2="1011"/>
      <line x1="677.4" y1="883.8" x2="677.4" y2="1011"/>
      <rect x="223.8" y="1011" width="453.6" height="28.2"/>
    </g>
    <g class="white-bands" fill="var(--paper)">
      <polygon points="67.8,178.8 108,178.8 136.8,226.2 67.8,226.2"/>
      <polygon points="441,178.8 692.4,178.8 692.4,226.2 471,226.2"/>
      <polygon points="186,398.4 515,398.4 515,445.2 214.8,445.2"/>
    </g>
  </svg>

  <p class="brand-name brand-name--lid">kolvu</p>
  <p class="tagline">Strength for your shoes<br>Comfort for your feet</p>
  <h1 class="product-title product-title--lid"><span class="solid">CREASE</span><span class="outline">GUARDS</span></h1>
  <div class="shoe-art shoe-art--lid" role="img" aria-label="Grey line drawing of a high-top sneaker"></div>
  <p class="size-mark">L</p>

  <p class="brand-name brand-name--flap">kolvu</p>

  <div class="shoe-art shoe-art--front" role="img" aria-label="Small grey line drawing of a sneaker"></div>
  <div class="upc-space" role="img" aria-label="Blank space reserved for the UPC"></div>
  <p class="brand-name brand-name--front">kolvu</p>

  <p class="brand-name brand-name--end">kolvu</p>

  <p class="brand-name brand-name--back">kolvu</p>
  <h2 class="product-title product-title--back"><span class="solid">CREASE</span><span class="outline">GUARDS</span></h2>
  <div class="shoe-art shoe-art--back" role="img" aria-label="Small grey line drawing of a sneaker, upside down"></div>
</main>
</body>
</html>
```